Need a Poster Design A3 for our Cricket Competition

We need a poster design for our upcoming T20 cricket competition Coastline Summer Cup (CSC).

it should say like this:

Bellwick Real Estate (logo supplied)
proudly presents

Coastline Summer Cup (logo supplied)

its a T20 cricket competition

starting 1st April 2018
Registrations Closing : 18th March

prizes worth $5000 to be won

for Registration contact: 0401937265 / 0402816394 and our Facebook page address..see last time's poster

and then sponsors
Updates

Hello.. We will be closing the contest earlier by 5 days so we need to get the design by Tuesday 13th Feb .. Thanks

Industry/Entity Type

Real Estate

Colors

Designer to choose colors to be used in the design.

Requirements
Must have
• emphasis on our main sponsor Bellwick Real Estate & our competition logo

```html
<!DOCTYPE html>
<html lang="en">
<head>
<meta charset="utf-8">
<title>Coastline Summer Cup – T20 Poster</title>
<link rel="stylesheet" href="https://fonts.googleapis.com/css2?family=Arimo:wght@400;700&family=Oswald:wght@400&family=Luckiest+Guy&display=swap">
<style>
  :root{
    --navy:#1b2462;
    --ink:#111111;
    --white:#ffffff;
    --red:#d8241f;
    --yellow:#f6c500;
    --sky:#9fb8e6;
    --grass:#6fbf2c;
    --panel:#ffffff;
    --brown:#2b2019;
    --gold:#b58a2e;
  }
  *{margin:0;padding:0;box-sizing:border-box}
  html,body{width:848px;height:1200px;overflow:hidden;background:#fff}
  .poster{position:relative;width:848px;height:1200px;overflow:hidden;font-family:'Arimo',Arial,sans-serif;color:var(--ink)}
  .backdrop{position:absolute;inset:0;
    background:
      radial-gradient(ellipse 60% 40% at 35% 25%, rgba(255,255,255,.85), rgba(255,255,255,0) 70%),
      linear-gradient(160deg, #4d6fd1 0%, var(--sky) 28%, #d9e4f3 42%, #a9d266 58%, var(--grass) 75%, #3f8a1e 100%);}
  .batsman{position:absolute;left:0;top:370px;width:330px;height:640px;
    background:radial-gradient(ellipse 50% 50% at 40% 55%, rgba(10,10,10,.85), rgba(10,10,10,.55) 60%, rgba(10,10,10,0) 100%);}
  .fireball{position:absolute;left:230px;top:700px;width:430px;height:210px;
    background:radial-gradient(ellipse 45% 50% at 75% 55%, #b8201c 0%, #e2542a 45%, rgba(245,160,40,.55) 70%, rgba(245,160,40,0) 100%);}

  .prize{position:absolute;left:22px;top:120px;transform:rotate(-24deg);transform-origin:left top;
    font-family:'Luckiest Guy',Impact,sans-serif;text-align:center;line-height:1}
  .prize-line{display:block;font-size:40px;color:var(--ink);letter-spacing:1px;-webkit-text-stroke:1px #fff}
  .prize-amount{display:block;font-size:44px;color:var(--red);-webkit-text-stroke:1px var(--ink);margin-top:4px;margin-left:40px}

  .sponsor-main{position:absolute;left:362px;top:38px;width:185px;height:186px;background:var(--navy);
    display:flex;flex-direction:column;align-items:center;justify-content:center;gap:10px;color:var(--white)}
  .sponsor-main .mark{width:22px;height:22px;background:var(--white)}
  .sponsor-main .name{font-size:17px;font-weight:400;text-align:center;line-height:1.25;letter-spacing:1px}

  .presents{position:absolute;left:0;width:900px;top:241px;text-align:center;font-size:24px;letter-spacing:.5px}

  .league{position:absolute;left:248px;top:295px;width:420px;height:190px;color:var(--navy)}
  .league .ball{position:absolute;left:0;top:38px;width:110px;height:110px;border-radius:50%;background:var(--red)}
  .league .short{position:absolute;left:128px;top:4px;font-size:128px;font-weight:700;line-height:1;letter-spacing:-2px}
  .league .full{position:absolute;left:0;top:154px;width:420px;font-size:25px;font-weight:700;letter-spacing:3px;text-align:center}

  .dates{position:absolute;left:532px;top:496px;width:316px;height:214px}
  .dates svg{position:absolute;inset:0}
  .dates .start{position:absolute;left:30px;right:0;top:20px;text-align:center;font-size:27px;font-weight:700;line-height:1.15;letter-spacing:1px}
  .dates .close{position:absolute;left:20px;right:0;top:118px;text-align:center;font-family:'Oswald',Arial,sans-serif;font-size:30px;line-height:1.2}

  .contact{position:absolute;left:310px;top:925px;width:530px;font-size:34px;letter-spacing:.5px;white-space:nowrap}
  .phones{position:absolute;left:393px;top:983px;font-size:33px;font-weight:700;color:var(--white);white-space:nowrap}

  .sponsor-panel{position:absolute;left:0;top:1010px;width:848px;height:190px}
  .sponsor{position:absolute;display:flex;align-items:center;justify-content:center;gap:6px;text-align:center;
    font-family:'Arimo',Arial,sans-serif;font-weight:700;line-height:1.1}
  .sponsor .dot{flex:none;border-radius:50%}
  .sponsor .sq{flex:none}
  .badge{flex:none;width:44px;height:50px;border-radius:10px;background:#2f6fb5}
  .small-label{display:block;font-size:5px;font-weight:400;letter-spacing:.3px;color:#333;margin-bottom:3px}
</style>
</head>
<body>
<main class="poster">
  <div class="backdrop" role="img" aria-label="Motion-blur background of blue sky and clouds sweeping into green grass"></div>
  <div class="batsman" role="img" aria-label="Black silhouette of a batsman in a helmet swinging a bat"></div>
  <div class="fireball" role="img" aria-label="Red cricket ball streaking forward with a trail of flames"></div>

  <div class="prize"><span class="prize-line">PRIZES WORTH</span><span class="prize-amount">$5000</span></div>

  <div class="sponsor-main">
    <span class="mark"></span>
    <span class="name">BELLWICK<br>REAL ESTATE</span>
  </div>

  <p class="presents">PROUDLY PRESENTS</p>

  <div class="league">
    <span class="ball"></span>
    <span class="short">CSC</span>
    <span class="full">COASTLINE SUMMER CUP</span>
  </div>

  <section class="dates">
    <svg viewBox="0 0 316 214" width="316" height="214" aria-hidden="true">
      <path d="M8 6 L316 0 L316 214 L22 208 L4 186 L14 160 L0 130 L12 104 L6 78 L18 52 L2 30 Z" fill="var(--yellow)"/>
    </svg>
    <p class="start">STARTING AT<br>APRIL 2018</p>
    <p class="close">REGISTRATION CLOSING:<br>18TH MARCH</p>
  </section>

  <p class="contact">FOR REGISTRATION CONTACT</p>
  <p class="phones">0401937265/0402816394</p>

  <section class="sponsor-panel" aria-label="Sponsors">
    <svg viewBox="0 0 848 190" width="848" height="190" style="position:absolute;inset:0" aria-hidden="true">
      <path d="M7 3 H364 V31 H848 V190 H7 Z" fill="var(--panel)"/>
    </svg>

    <div class="sponsor" style="left:17px;top:18px;width:120px;height:92px;font-size:15px;color:#2f6fb5;flex-direction:column;gap:4px">
      <span class="badge"></span>Keystone Services
    </div>
    <div class="sponsor" style="left:141px;top:26px;width:104px;height:76px;font-size:19px;font-weight:400;color:var(--ink)">Verda<br>Organic Cotton</div>
    <div class="sponsor" style="left:258px;top:16px;width:91px;height:90px;background:var(--brown);font-size:12px;font-weight:400;color:var(--gold);letter-spacing:2px">SORREL</div>
    <div class="sponsor" style="left:410px;top:22px;width:137px;height:88px;font-size:16px;color:var(--ink);flex-direction:column;gap:6px">
      <span class="sq" style="width:26px;height:26px;background:var(--ink)"></span>HARLOW FAMILY TRUST
    </div>
    <div class="sponsor" style="left:577px;top:20px;width:150px;height:90px;font-size:18px;color:#a8832c;flex-direction:column;gap:4px">
      Honeyleaf Sweets<br><span style="font-size:12px;font-weight:700;color:#a8832c;letter-spacing:2px">GLENHAVEN</span>
    </div>
    <div class="sponsor" style="left:740px;top:40px;width:82px;height:50px;font-size:26px;color:var(--ink);flex-direction:column;gap:0">
      <span class="small-label">SINGLE COLOUR VERSION</span>QT
    </div>

    <div class="sponsor" style="left:26px;top:120px;width:222px;height:62px;font-size:32px;color:var(--ink)">
      Brightline TV<span class="dot" style="width:16px;height:16px;background:#e8332a"></span>
    </div>
    <div class="sponsor" style="left:268px;top:116px;width:112px;height:70px;font-size:13px;color:var(--white);background:var(--red);flex-direction:column;gap:2px">
      PANTRY<br><span style="font-size:8px;font-weight:700;color:var(--white)">GROCERIES &amp; SPICES</span>
    </div>
    <div class="sponsor" style="left:402px;top:126px;width:175px;height:50px;font-size:20px;color:var(--ink)">
      <span class="dot" style="width:14px;height:14px;background:var(--red)"></span>Northway Transport
    </div>
    <div class="sponsor" style="left:594px;top:118px;width:133px;height:68px;font-size:17px;color:#b8201c;flex-direction:column;gap:3px">
      RIDGELINE FREIGHT
      <span style="display:block;width:133px;background:#b8201c;color:var(--white);font-size:7px;padding:3px 4px;text-align:left;line-height:1.3">DEV MALHOTRA &nbsp; 0491 570 156<br>AMAN SETHI &nbsp;&nbsp;&nbsp;&nbsp;&nbsp; 0491 570 110</span>
    </div>
    <div class="sponsor" style="left:740px;top:126px;width:82px;height:50px;font-size:26px;color:#f0932b;flex-direction:column;gap:0">
      <span class="small-label">DOUBLE COLOUR VERSION</span>QT
    </div>
  </section>
</main>
</body>
</html>
```